Flyer Design Project

Business is Wexford In Home Care

We are an Australian provider of In Home Care services.

We have a focus on quality care and a high standard of service.

We are non medical

We want to promote the health, happiness and independence of senior citizens by providing some help at home for general domestic duties (cleaning, bed linnen), personal care (showering, grooming) and meal preparation etc.

Target Market(s)

Seniors (70+) and the Children of seniors.

Industry/Entity Type

Business

Requirements
Must have
• Colour scheme from our website (www.wexfordinhomecare.com.au) –

The uploaded Word doc contains the desired copy.

Leaflet will be a standard A4 size foldout with 6 panels, 3 on each side.

```html
<!DOCTYPE html>
<html lang="en">
<head>
<meta charset="utf-8">
<title>Wexford In Home Care – Flyer</title>
<link rel="stylesheet" href="https://fonts.googleapis.com/css2?family=Arimo:wght@400;700&display=swap">
<style>
  :root {
    --sky: #cfe2f6;
    --sky-deep: #b9d4f0;
    --sky-pale: #e6f0fb;
    --navy: #1d2b5c;
    --royal: #1560bd;
    --ink: #2a2c48;
    --orange: #f5a623;
    --white: #ffffff;
    --teal: #2f8fb0;
    --photo-warm: #d9c3ae;
    --photo-dark: #1a1a1a;
  }
  * { box-sizing: border-box; margin: 0; padding: 0; }
  html, body { width: 1200px; height: 854px; overflow: hidden; }
  body { font-family: "Arimo", Arial, sans-serif; color: var(--ink); }
  .flyer {
    position: relative; width: 1200px; height: 854px; overflow: hidden;
    background: radial-gradient(ellipse at 50% 40%, var(--sky-pale) 0%, var(--sky) 55%, var(--sky-deep) 100%);
  }
  .panel-divider { position: absolute; top: 0; width: 1px; height: 854px; background: rgba(255,255,255,0.35); }
  .photo {
    position: absolute; border-radius: 12px; outline: 2px dashed rgba(255,255,255,0.9); outline-offset: 6px;
  }
  .photo--carer-man { left: 52px; top: 28px; width: 341px; height: 240px; background: linear-gradient(135deg, #ece6df, var(--photo-warm) 60%, #b8a38f); }
  .photo--hands { left: 432px; top: 28px; width: 340px; height: 208px; background: radial-gradient(circle at 50% 55%, #c0507e 0%, #7a3a3a 22%, var(--photo-dark) 48%); }
  .photo--carer-woman { left: 826px; top: 120px; width: 342px; height: 208px; background: linear-gradient(135deg, #efe9e2, #dccbb9 55%, #c9b29c); }

  .swoosh { position: absolute; left: 0; top: 0; }

  .heading-pill {
    position: absolute; background: var(--white); border-radius: 0 18px 18px 0;
    font-weight: 700; color: var(--navy); font-size: 24px; line-height: 34px; padding: 0 16px 0 6px;
  }
  .bullet { display: inline-block; width: 11px; height: 11px; border-radius: 50%; background: var(--navy); margin-right: 3px; vertical-align: 1px; }
  .bullet--gold { background: var(--orange); width: 14px; height: 14px; margin-right: 6px; }

  .service-list { position: absolute; left: 40px; top: 360px; width: 332px; list-style: none; }
  .service-list__name { color: var(--royal); font-weight: 700; font-size: 16px; line-height: 22px; }
  .service-list__desc { font-size: 15.5px; line-height: 24px; padding-left: 6px; text-align: justify; margin-bottom: 1px; }

  .tagline { position: absolute; left: 40px; top: 766px; width: 340px; text-align: center; font-size: 24px; font-weight: 700; color: var(--navy); line-height: 30px; }

  .intro { position: absolute; left: 403px; top: 263px; width: 394px; text-align: center; font-weight: 700; font-size: 16px; color: var(--navy); }
  .service-index { position: absolute; left: 452px; top: 366px; list-style: none; }
  .service-index li { font-weight: 700; font-size: 19px; color: var(--royal); height: 31px; line-height: 27px; }

  .contact-band { position: absolute; left: 403px; top: 560px; width: 394px; height: 294px; }
  .call { position: absolute; left: 403px; top: 648px; width: 394px; text-align: center; font-size: 31px; font-weight: 700; color: var(--navy); }
  .contact-line { position: absolute; left: 403px; width: 394px; text-align: center; font-size: 15.5px; color: var(--navy); }
  .label { background: var(--white); border-radius: 6px; padding: 0 4px; font-weight: 700; margin-right: 4px; }

  .brand { position: absolute; left: 822px; top: 40px; display: flex; align-items: center; gap: 12px; }
  .brand__mark { width: 40px; height: 40px; border-radius: 50%; background: var(--navy); }
  .brand__name { font-size: 22px; color: var(--navy); font-weight: 400; }

  .offer-badge { position: absolute; left: 855px; top: 370px; width: 281px; height: 66px; border-radius: 33px; background: var(--orange); color: var(--white); text-align: center; font-weight: 700; }
  .offer-badge__title { font-size: 29px; line-height: 36px; padding-top: 2px; }
  .offer-badge__sub { font-size: 20px; line-height: 22px; }

  .quality { position: absolute; left: 880px; height: 32px; line-height: 32px; padding: 0 20px 0 14px; background: var(--white); border-radius: 16px; font-weight: 700; font-size: 22px; color: var(--navy); }
  .quality::before { content: ""; position: absolute; left: -30px; top: 6px; width: 20px; height: 20px; border-radius: 50%; background: rgba(255,255,255,0.75); }

  .comfort { position: absolute; left: 800px; top: 744px; width: 400px; text-align: center; font-size: 23px; font-weight: 700; color: var(--navy); line-height: 30px; }
</style>
</head>
<body>
<main class="flyer">
  <div class="panel-divider" style="left:400px"></div>
  <div class="panel-divider" style="left:800px"></div>

  <svg class="swoosh" width="1200" height="854" viewBox="0 0 1200 854" aria-hidden="true">
    <defs>
      <linearGradient id="band" x1="0" y1="0" x2="0" y2="1">
        <stop offset="0" stop-color="#ffffff" stop-opacity="0.95"/>
        <stop offset="0.55" stop-color="#eaf3fc"/>
        <stop offset="1" stop-color="#7fb6e6"/>
      </linearGradient>
    </defs>
    <path d="M403 854 V640 C470 570 560 570 620 600 C690 636 760 650 797 600 V854 Z" fill="url(#band)"/>
    <path d="M760 560 C880 560 960 640 1080 690 C1140 712 1180 700 1200 690" fill="none" stroke="var(--teal)" stroke-width="6" opacity="0.8"/>
    <path d="M800 600 C900 640 1000 720 1120 700" fill="none" stroke="#5aa4d4" stroke-width="3" opacity="0.8"/>
    <path d="M800 640 C880 700 960 720 1200 700 V660 C1100 690 1000 670 800 600 Z" fill="#4a9ad6" opacity="0.35"/>
    <path d="M390 560 C430 600 470 620 540 600" fill="none" stroke="var(--teal)" stroke-width="2" opacity="0.7"/>
  </svg>

  <div class="photo photo--carer-man" role="img" aria-label="Smiling carer beside an elderly man"></div>
  <div class="photo photo--hands" role="img" aria-label="Cupped hands holding a pink flower on a black background"></div>
  <div class="photo photo--carer-woman" role="img" aria-label="Carer with her hands on the shoulders of a smiling elderly woman"></div>

  <!-- Inside left panel -->
  <h2 class="heading-pill" style="left:80px;top:314px">Our services</h2>
  <ul class="service-list">
    <li><div class="service-list__name"><span class="bullet"></span>Personal care</div><div class="service-list__desc">showering, dressing, hygiene and grooming</div></li>
    <li><div class="service-list__name"><span class="bullet"></span>Domestic Assistance</div><div class="service-list__desc">general cleaning, laundry, bed linen and ironing</div></li>
    <li><div class="service-list__name"><span class="bullet"></span>Meal Preparation</div><div class="service-list__desc">support to select, prepare and enjoy meals</div></li>
    <li><div class="service-list__name"><span class="bullet"></span>Respite</div><div class="service-list__desc">support for carers to take a well-earned break</div></li>
    <li><div class="service-list__name"><span class="bullet"></span>Companionship</div><div class="service-list__desc">visits, social outings, transport to appointments and support shopping</div></li>
    <li><div class="service-list__name"><span class="bullet"></span>Rehabilitation</div><div class="service-list__desc">support after surgery or recovering from illness</div></li>
  </ul>
  <p class="tagline">Reliable, compassionate,<br>person centred</p>

  <!-- Back panel -->
  <p class="intro">Providing Exceptional Care at home</p>
  <h2 class="heading-pill" style="left:480px;top:325px">Our services</h2>
  <ul class="service-index">
    <li><span class="bullet bullet--gold"></span>Personal Care</li>
    <li><span class="bullet bullet--gold"></span>Domestic Assistance</li>
    <li><span class="bullet bullet--gold"></span>Meal Preparation</li>
    <li><span class="bullet bullet--gold"></span>Respite</li>
    <li><span class="bullet bullet--gold"></span>Companionship</li>
    <li><span class="bullet bullet--gold"></span>Rehabilitation Support</li>
  </ul>
  <p class="call">CALL 1300 555 214</p>
  <p class="contact-line" style="top:706px"><span class="label">E</span>contact@wexfordinhomecare.com.au</p>
  <p class="contact-line" style="top:729px"><span class="label">W</span>wexfordinhomecare.com.au</p>
  <p class="contact-line" style="top:777px"><span class="label">Address</span>27A/318 Harbour Lane</p>
  <p class="contact-line" style="top:800px">Sydney NSW 2000</p>

  <!-- Front cover -->
  <div class="brand"><span class="brand__mark"></span><span class="brand__name">Wexford In Home Care</span></div>
  <div class="offer-badge">
    <div class="offer-badge__title">In Home Care</div>
    <div class="offer-badge__sub">specialistsoffering</div>
  </div>
  <div class="quality" style="top:463px">professional</div>
  <div class="quality" style="top:519px">non-medical</div>
  <div class="quality" style="top:573px">companion based care</div>
  <p class="comfort">in the comfort and<br>familiarity of your home.</p>
</main>
</body>
</html>
```